Business Card Design for a Sound engineer and DJ

We would like a residn of the business card.

Logo must remain the same.
The card is for the owner of the company.
The business card is in Arabic as the company is based in Kuwait.
The company specializes in sound engineering for singers concerts and events and in addition DJ.
The color options is up to the designer but we would like it masculine as the owner is a man.

Target Market(s)

All ages

Industry/Entity Type

Media

Contact Information for Business Card

Name:
Eng. Tarek Halabi
م/طارق حلبي

The name above is in Arabic and English.

Title: General Manager
Mobile: +965 66307852
Office: +965 22486037
Email: info@sawtarin.net

Address:
Office no. 3
1st floor
Almarfa Complex
Rashed AlQeblawi St.
Salmiya
Kuwait

Instagram: @sawtarin
Snap: sawtarin

Requirements
Nice to have
• can we have Instagram icon and snap icon and a phone vector and email?
• Instead of writing the words

```html
<!DOCTYPE html>
<html lang="en">
<head>
<meta charset="utf-8">
<title>Sawtarin – Business Card</title>
<link rel="stylesheet" href="https://fonts.googleapis.com/css2?family=Source+Sans+3:wght@300;400;600&family=Noto+Sans+Arabic:wght@400&display=swap">
<style>
  :root {
    --bg: #e9e6e2;
    --card-dark: #140709;
    --card-mid: #2a1d21;
    --card-sheen: #4a3c40;
    --name: #6c7ee6;
    --lavender: #b7a2ea;
    --violet: #a58ae2;
    --pink: #d57ee8;
    --line: #7d74d8;
    --icon: #9c8ce0;
  }
  * { margin: 0; padding: 0; box-sizing: border-box; }
  html, body { width: 1200px; height: 1062px; overflow: hidden; }
  body {
    background: var(--bg);
    font-family: "Source Sans 3", "Noto Sans Arabic", sans-serif;
    position: relative;
  }
  .card {
    position: absolute;
    left: 170px;
    width: 860px;
    height: 480px;
    border-radius: 4px;
    background:
      radial-gradient(ellipse 55% 70% at 38% 45%, var(--card-sheen) 0%, rgba(74,60,64,0) 70%),
      linear-gradient(135deg, var(--card-dark) 0%, var(--card-mid) 55%, var(--card-dark) 100%);
    box-shadow: 0 10px 28px rgba(0,0,0,.28);
    overflow: hidden;
  }
  .card--front { top: 36px; }
  .card--back { top: 546px; }

  /* front side */
  .holder { position: absolute; left: 60px; top: 120px; }
  .holder__name { font-size: 40px; font-weight: 600; color: var(--name); line-height: 1; }
  .holder__title {
    margin-top: 6px; padding-top: 6px;
    border-top: 2px solid var(--line);
    font-size: 26px; font-weight: 300; color: var(--violet);
    display: inline-block;
  }
  .contacts { position: absolute; left: 60px; top: 250px; list-style: none; }
  .contacts li {
    display: flex; align-items: center; gap: 12px;
    font-size: 21px; color: var(--lavender); line-height: 29px;
  }
  .contacts svg { width: 16px; height: 16px; flex: none; }
  .divider {
    position: absolute; left: 60px; top: 400px; width: 560px; height: 2px;
    background: var(--line);
  }
  .address {
    position: absolute; left: 60px; top: 410px;
    font-size: 22px; color: var(--violet); line-height: 28px;
  }
  .brand { position: absolute; text-align: left; }
  .card--front .brand { right: 60px; top: 70px; text-align: right; }
  .brand__mark { display: inline-flex; align-items: center; gap: 14px; }
  .brand__square { width: 22px; height: 22px; background: var(--pink); }
  .brand__name {
    font-size: 44px; font-weight: 400; letter-spacing: 8px; color: var(--violet);
  }
  .brand__tag {
    margin-top: 6px; font-size: 15px; letter-spacing: 3px; color: var(--lavender);
  }
  .brand__tag-ar {
    font-family: "Noto Sans Arabic", sans-serif; direction: rtl;
    font-size: 16px; color: var(--lavender); margin-top: 2px;
  }

  /* back side */
  .card--back .brand {
    left: 0; right: 0; top: 170px; text-align: center;
  }
  .card--back .brand__name { font-size: 64px; letter-spacing: 12px; }
  .card--back .brand__square { width: 30px; height: 30px; }
  .card--back .brand__tag { font-size: 18px; }
  .card--back .brand__tag-ar { font-size: 19px; }
</style>
</head>
<body>

<section class="card card--front" aria-label="Business card front">
  <div class="brand">
    <div class="brand__mark">
      <span class="brand__square"></span>
      <span class="brand__name">SAWTARIN</span>
    </div>
    <p class="brand__tag">DJ . SOUND ENG. . LIGHTING</p>
    <p class="brand__tag-ar">دي جي . هندسة صوت . إضاءة</p>
  </div>

  <div class="holder">
    <p class="holder__name">Tarek Halabi</p>
    <p class="holder__title">General Manager</p>
  </div>

  <ul class="contacts">
    <li>
      <svg viewBox="0 0 16 16"><rect x="4" y="1" width="8" height="14" rx="1.5" fill="none" stroke="var(--icon)" stroke-width="1.6"/><circle cx="8" cy="12.5" r="0.9" fill="var(--icon)"/></svg>
      +965 66307852
    </li>
    <li>
      <svg viewBox="0 0 16 16"><path d="M4 1.5 6.5 4 5 6c.8 2 2.5 3.8 5 5l2-1.5 2.5 2.5-1.8 2.3C7 14 2 9 1.7 3.3Z" fill="var(--icon)"/></svg>
      +965 22486037
    </li>
    <li>
      <svg viewBox="0 0 16 16"><text x="8" y="13" text-anchor="middle" font-size="15" font-family="sans-serif" fill="var(--icon)">@</text></svg>
      info@sawtarin.net
    </li>
    <li>
      <svg viewBox="0 0 16 16"><rect x="2" y="2" width="12" height="12" fill="var(--icon)"/></svg>
      @sawtarin
    </li>
    <li>
      <svg viewBox="0 0 16 16"><circle cx="8" cy="8" r="6" fill="var(--icon)"/></svg>
      sawtarin
    </li>
  </ul>

  <div class="divider"></div>
  <p class="address">Office no. 3 1st floor Almarfa Complex<br>Rashed AlQeblawi St. Salmiya Kuwait</p>
</section>

<section class="card card--back" aria-label="Business card back">
  <div class="brand">
    <div class="brand__mark">
      <span class="brand__square"></span>
      <span class="brand__name">SAWTARIN</span>
    </div>
    <p class="brand__tag">DJ . SOUND ENG. . LIGHTING</p>
    <p class="brand__tag-ar">دي جي . هندسة صوت . إضاءة</p>
  </div>
</section>

</body>
</html>
```